Norvane Builders Business Card

Modern and Professional Business Card for a Med size construction/development company.

See the samples below for the design I like … but I need ideas for incorporating the red company logo while still keeping the clean look of the card samples that are attached.

Logo and tag line on the back … info on the front.

Tagline: Built Right from Every Foundation

Target Market(s)

Med-Large General Contractors

Contact Information for Business Card

Norvane Builders Limited
42 Brenton Street
Elk Harbour, NL
B3K 7T2

t: 709-555-0147
f: 709-555-0192
w: www.norvanebuilders-example.com

Font styles to use
Sans Serif

Colors
fbee3e

Requirements
Must have
• I like the black and yellow designs of the attached samples …. but I'm not sure how to incorporate the red Norvane Builders logo into that design??
Nice to have
• Construction safety strips

```html
<!DOCTYPE html>
<html lang="en">
<head>
<meta charset="utf-8">
<title>Norvane Builders Business Card</title>
<link href="https://fonts.googleapis.com/css2?family=Lato:wght@400;700;900&display=swap" rel="stylesheet">
<style>
  :root {
    --brand-red: #e31e26;
    --brand-red-dark: #c8151c;
    --ink: #2b2b2b;
    --ink-soft: #444444;
    --paper: #ffffff;
    --swoosh: #efefef;
    --rule: #b9b9b9;
    --stage: #2e2e2e;
  }
  * { box-sizing: border-box; margin: 0; padding: 0; }
  html, body {
    width: 1200px; height: 866px; overflow: hidden;
    background: var(--stage);
    font-family: "Lato", Arial, sans-serif;
  }
  .sheet {
    width: 1200px; height: 866px;
    display: flex; align-items: center; justify-content: center; gap: 40px;
  }
  .card {
    position: relative;
    width: 540px; height: 309px;
    overflow: hidden;
    box-shadow: 0 10px 24px rgba(0,0,0,.45);
  }
  .card__swoosh { position: absolute; inset: 0; width: 100%; height: 100%; }

  /* Front */
  .card--front { background: var(--paper); }
  .card--front .card__band {
    position: absolute; left: 0; right: 0; bottom: 0; height: 10px;
    background: var(--brand-red);
  }
  .contact { position: absolute; left: 34px; top: 74px; }
  .contact__name {
    color: var(--brand-red); font-weight: 900; font-size: 20px;
    letter-spacing: .5px; text-transform: uppercase; line-height: 24px;
  }
  .contact__title {
    color: var(--ink-soft); font-size: 13px; margin-top: 1px; letter-spacing: .3px;
  }
  .contact__list { list-style: none; margin-top: 10px; }
  .contact__item {
    display: flex; align-items: center; gap: 6px;
    color: var(--ink); font-size: 12.5px; line-height: 19px; letter-spacing: .2px;
  }
  .contact__icon { width: 11px; height: 11px; fill: var(--brand-red); flex: none; }
  .card__rule {
    position: absolute; left: 244px; top: 88px; width: 266px; height: 1px;
    background: var(--rule); transform: rotate(4deg); transform-origin: left center;
  }
  .wordmark {
    position: absolute; right: 34px; top: 124px;
    display: flex; align-items: center; gap: 8px;
  }
  .wordmark__square { width: 12px; height: 12px; background: var(--brand-red); }
  .wordmark__name {
    color: var(--brand-red); font-weight: 900; font-size: 22px;
    letter-spacing: .5px; text-transform: uppercase; line-height: 1;
  }
  .address {
    position: absolute; right: 34px; bottom: 30px; text-align: right; font-style: normal;
  }
  .address__company { color: var(--brand-red); font-weight: 700; font-size: 13.5px; letter-spacing: .3px; }
  .address__line { color: var(--ink); font-size: 13px; line-height: 17px; letter-spacing: .3px; }

  /* Back */
  .card--back { background: var(--brand-red); }
  .back__center {
    position: absolute; inset: 0;
    display: flex; flex-direction: column; align-items: center; justify-content: center; gap: 22px;
  }
  .back__wordmark { display: flex; align-items: center; gap: 10px; }
  .back__square { width: 18px; height: 18px; background: var(--paper); }
  .back__name {
    color: var(--paper); font-weight: 900; font-size: 34px;
    letter-spacing: 1px; text-transform: uppercase; line-height: 1;
  }
  .back__tagline {
    color: var(--paper); font-size: 13px; font-weight: 700;
    letter-spacing: 1.2px; text-transform: uppercase;
  }
</style>
</head>
<body>
<main class="sheet">

  <section class="card card--front" aria-label="Business card front">
    <svg class="card__swoosh" viewBox="0 0 540 309" aria-hidden="true">
      <path d="M150 0 C 230 90, 270 190, 250 309 L 300 309 C 300 190, 260 80, 190 0 Z" fill="var(--swoosh)"/>
      <path d="M110 0 C 170 70, 200 140, 200 200 C 215 140, 190 60, 140 0 Z" fill="#f5f5f5"/>
    </svg>

    <div class="contact">
      <h1 class="contact__name">Daniel Whitmore</h1>
      <p class="contact__title">Managing Director</p>
      <ul class="contact__list">
        <li class="contact__item">
          <svg class="contact__icon" viewBox="0 0 16 16"><path d="M3.5 1 L6 1 L7 5 L5.3 6.3 C6 8 8 10 9.7 10.7 L11 9 L15 10 L15 12.5 C15 14 14 15 12.5 15 C6.5 15 1 9.5 1 3.5 C1 2 2 1 3.5 1 Z"/></svg>
          709-555-0147
        </li>
        <li class="contact__item">
          <svg class="contact__icon" viewBox="0 0 16 16"><rect x="4" y="1" width="8" height="5"/><rect x="1" y="6" width="14" height="6" rx="1"/><rect x="4" y="10" width="8" height="5"/></svg>
          709-555-0192
        </li>
        <li class="contact__item">
          <svg class="contact__icon" viewBox="0 0 16 16"><circle cx="8" cy="8" r="7"/><path d="M1 8 H15 M8 1 C5 4 5 12 8 15 M8 1 C11 4 11 12 8 15" stroke="#fff" stroke-width="1" fill="none"/></svg>
          www.norvanebuilders-example.com
        </li>
      </ul>
    </div>

    <div class="card__rule"></div>

    <div class="wordmark">
      <span class="wordmark__square"></span>
      <span class="wordmark__name">Norvane Builders</span>
    </div>

    <address class="address">
      <p class="address__company">Norvane Builders Limited</p>
      <p class="address__line">42 Brenton Street</p>
      <p class="address__line">Elk Harbour, NL B3K 7T2</p>
    </address>

    <div class="card__band"></div>
  </section>

  <section class="card card--back" aria-label="Business card back">
    <svg class="card__swoosh" viewBox="0 0 540 309" aria-hidden="true">
      <path d="M150 0 C 230 90, 270 190, 250 309 L 300 309 C 300 190, 260 80, 190 0 Z" fill="var(--brand-red-dark)" opacity=".45"/>
    </svg>
    <div class="back__center">
      <div class="back__wordmark">
        <span class="back__square"></span>
        <span class="back__name">Norvane Builders</span>
      </div>
      <p class="back__tagline">Built Right from Every Foundation</p>
    </div>
  </section>

</main>
</body>
</html>
```